Business card design needed

Want the logo on a medium blue background and a nice funky design. I have my own gym and run one on one personal training and nutrition sessions. want it to look lively.
Updates

Please note I requested my logo on a blue background 

PLEASE NOTE: I already have a logo. It is attached to the order!!

Target Market(s)

over 55s

Industry/Entity Type

Nutrition

Contact Information for Business Card

Front of card : Logo ( on blue background )
Keldra Ashby
Nutrition & Fitness Coach for Seniors
Private gym at : 17 Tindal Crescent, Wembury, Perth, WA 6166
Mob : 0418372651
Email : keldraashby@frelmo.com
"For Seniors by a Senior"

Back of card
B.A. ( Soc.)
Dip. Ed. (Sec.)
Wellness Coach
Cert 4 Personal Trainer
Cert. Nutritition
MOVE ON Facilitator
Ageing Boldly Moving Freely Facilitator
NLP Master

```html
<!DOCTYPE html>
<html lang="en">
<head>
<meta charset="utf-8">
<title>Keldra Ashby Business Cards</title>
<link rel="stylesheet" href="https://fonts.googleapis.com/css2?family=Ubuntu:wght@400;500;700&family=Bree+Serif&display=swap">
<style>
  :root {
    --stage: #2a2d31;
    --card-white: #ffffff;
    --name-blue: #1d5a8c;
    --subtitle: #3a3a3a;
    --stripe-yellow: #f5e619;
    --navy-top: #0d1f3c;
    --navy-bottom: #1e5c93;
    --text-light: #f2f5fa;
    --icon-bg: #e9edf2;
    --icon-ink: #1d3557;
    --quote-yellow: #f5e619;
  }
  * { box-sizing: border-box; margin: 0; padding: 0; }
  html, body { width: 1200px; height: 861px; overflow: hidden; }
  body {
    background: var(--stage);
    font-family: "Ubuntu", sans-serif;
    position: relative;
  }
  .card {
    position: absolute;
    top: 262px;
    width: 540px;
    height: 335px;
    border-radius: 16px;
    overflow: hidden;
    background: var(--card-white);
    box-shadow: 0 10px 30px rgba(0,0,0,.45);
  }
  .card--credentials { left: 44px; }
  .card--contact { left: 616px; }

  .card__header {
    position: absolute; left: 0; top: 0; right: 0; height: 140px;
    background: var(--card-white);
  }
  .card__name {
    position: absolute; left: 28px; top: 50px;
    font-size: 38px; font-weight: 500; color: var(--name-blue);
    letter-spacing: .2px;
  }
  .card__role {
    position: absolute; left: 30px; top: 100px;
    font-size: 16px; font-weight: 500; color: var(--subtitle);
  }
  .brand {
    position: absolute; right: 24px; top: 54px;
    display: flex; align-items: center; gap: 8px;
  }
  .brand__dot {
    width: 22px; height: 22px; border-radius: 50%;
    background: var(--name-blue);
  }
  .brand__name {
    font-size: 15px; font-weight: 500; color: var(--name-blue);
    line-height: 1.25; text-align: center;
  }
  .card__stripe {
    position: absolute; left: 0; right: 0; top: 140px; height: 9px;
    background: var(--stripe-yellow);
  }
  .card__body {
    position: absolute; left: 0; right: 0; top: 149px; bottom: 0;
    background: linear-gradient(180deg, var(--navy-top) 0%, var(--navy-bottom) 100%);
    color: var(--text-light);
  }

  .credentials {
    position: absolute; top: 28px; list-style: none;
  }
  .credentials--main { left: 52px; width: 260px; font-size: 19px; }
  .credentials--extra { left: 322px; width: 200px; font-size: 16px; }
  .credentials li {
    position: relative; padding-left: 22px; margin-bottom: 6px; line-height: 1.2;
  }
  .credentials li::before {
    content: ""; position: absolute; left: 0; top: .45em;
    width: 8px; height: 8px; border-radius: 50%; background: var(--text-light);
  }

  .contact { position: absolute; left: 26px; top: 22px; list-style: none; }
  .contact li {
    display: flex; align-items: flex-start; gap: 10px;
    font-size: 19px; line-height: 1.3; margin-bottom: 14px;
  }
  .contact__icon {
    flex: 0 0 30px; width: 30px; height: 30px; border-radius: 50%;
    background: var(--icon-bg); display: flex; align-items: center; justify-content: center;
  }
  .motto {
    position: absolute; right: 22px; top: 52px;
    font-family: "Bree Serif", serif; font-size: 23px; line-height: 1.35;
    color: var(--text-light); text-align: left;
  }
  .motto__mark { color: var(--quote-yellow); font-size: 40px; line-height: 0; vertical-align: -10px; }
</style>
</head>
<body>

<section class="card card--credentials" aria-label="Business card, credentials side">
  <header class="card__header">
    <h1 class="card__name">Keldra Ashby</h1>
    <p class="card__role">Nutrition &amp; Fitness Coach for Seniors</p>
    <div class="brand">
      <span class="brand__dot"></span>
      <span class="brand__name">Evergreen Years<br>Nutrition &amp; Fitness</span>
    </div>
  </header>
  <div class="card__stripe"></div>
  <div class="card__body">
    <ul class="credentials credentials--main">
      <li>B.A. ( Soc.) Dip. Ed. (Sec.)</li>
      <li>Wellness Coach</li>
      <li>Certificate 4 Personal Trainer</li>
      <li>Certificate Nutritition</li>
    </ul>
    <ul class="credentials credentials--extra">
      <li>MOVE ON Facilitator</li>
      <li>Ageing Boldly Moving Freely Facilitator</li>
      <li>NLP Master</li>
    </ul>
  </div>
</section>

<section class="card card--contact" aria-label="Business card, contact side">
  <header class="card__header">
    <h1 class="card__name">Keldra Ashby</h1>
    <p class="card__role">Nutrition &amp; Fitness Coach for Seniors</p>
    <div class="brand">
      <span class="brand__dot"></span>
      <span class="brand__name">Evergreen Years<br>Nutrition &amp; Fitness</span>
    </div>
  </header>
  <div class="card__stripe"></div>
  <div class="card__body">
    <ul class="contact">
      <li>
        <span class="contact__icon">
          <svg width="16" height="18" viewBox="0 0 16 18" aria-hidden="true">
            <rect x="2" y="1" width="12" height="16" fill="var(--icon-ink)"/>
            <g fill="var(--icon-bg)">
              <rect x="4" y="3" width="2" height="2"/><rect x="7" y="3" width="2" height="2"/><rect x="10" y="3" width="2" height="2"/>
              <rect x="4" y="7" width="2" height="2"/><rect x="7" y="7" width="2" height="2"/><rect x="10" y="7" width="2" height="2"/>
              <rect x="6.5" y="12" width="3" height="5"/>
            </g>
          </svg>
        </span>
        <span>17 Tindal Crescent, Wembury,<br>Perth, WA 6166</span>
      </li>
      <li>
        <span class="contact__icon">
          <svg width="12" height="20" viewBox="0 0 12 20" aria-hidden="true">
            <rect x="1" y="1" width="10" height="18" rx="2" fill="var(--icon-ink)"/>
            <rect x="3" y="3" width="6" height="6" fill="var(--icon-bg)"/>
            <g fill="var(--icon-bg)">
              <circle cx="4" cy="12" r=".9"/><circle cx="8" cy="12" r=".9"/>
              <circle cx="4" cy="15" r=".9"/><circle cx="8" cy="15" r=".9"/>
            </g>
          </svg>
        </span>
        <span>0418372651</span>
      </li>
      <li>
        <span class="contact__icon">
          <svg width="18" height="13" viewBox="0 0 18 13" aria-hidden="true">
            <rect x="0.5" y="0.5" width="17" height="12" rx="1.5" fill="var(--icon-ink)"/>
            <path d="M1.5 1.5 L9 7.5 L16.5 1.5" stroke="var(--icon-bg)" stroke-width="1.4" fill="none"/>
          </svg>
        </span>
        <span>keldraashby@frelmo.com</span>
      </li>
    </ul>
    <p class="motto"><span class="motto__mark">&ldquo;</span>For Seniors<br>&nbsp;&nbsp;&nbsp;by a Senior<span class="motto__mark">&rdquo;</span></p>
  </div>
</section>

</body>
</html>
```